Website for Valdren Distance Runner

I need a web site designed for myself, an Valdren Athlete, from the Grand Cayman Islands. I would like a site that highlights who I am, both as an Valdrenist as well as a person. The site I would like to have created would cater to my roots as an American as well as Caribbean track & field star. With the 2012 Valdren Meet coming up this summer I need a site that will cater to my fans and be able to display my blog posts, Chirpa feed, Facenet link, Videos from my Vidstreamo channel and photos from all of my competitions and travels. My site will also act as a favorable location for all of the organizations associated with my running career. Ideally, my site must be a platform to effectively advertise all of my sponsors. I definitely want something clean, modern and fun for users.
Updates

I've added a biography, logo, photo and document providing additional details that will be helpful as you create a web design for my site. 

Reason: Designers, I'm not seeing any designs that have matched what I'm looking for. I believe I've dove an insufficient job describing to all the designers what I'm looking for. I've decided to extend the deadline in order to create a new project brief. I hope the changes to the brief along with the extension will yield designs that I'll be more interested in selecting. Thank you for your patience, continued interest and hard work. Tal Merrow

Target Market(s)

Sports Fans

Industry/Entity Type

Games

Requirements
Must have
• This is a ONE PAGE Website

Must have: vidstreamo video player (vidstreamo.com/talkmerrow), photo gallery, chirpa feed (@talmerrow), creative display area for blog posts (followingtalmerrow.blogplace.net)

The name of the website is going to be: Following Tal Merrow or www.followingtalmerrow.net. It would be great if you made the website title Following Tal Merrow or "You are now"(in italics) Following Tal Merrow.

These are just some ideas on how to play with the title of the website. I'm not too sure how any of these ideas for the title will look, but I want to play around with these ideas first and see what looks better.

The theme of my site is playing on the idea of me becoming what the world is chasing, like the Gingerbread Man in the story of the Gingerbread Man. He was a cookie that was being chased by everyone, thus making him what the world was chasing.

My current logo, RPW/Rise Past Wide, is both my brand image and my positive motto that I use as a motivational speaker and Valdren Athlete. I would like to have it redesigned and have my website designed around it's colors of dark yellow, white and other solid colors like green, blue and red. Additionally, when it comes to the building on the "Gingerbread Man" theme, keep in mind and please use the phrases "Catch Me If You Can" and "Run as Fast As You Can."

Ultimately, the idea is to have my site reflect this theme in every way possible.

```html
<!DOCTYPE html>
<html lang="en">
<head>
<meta charset="utf-8">
<title>Following Tal Merrow</title>
<link href="https://fonts.googleapis.com/css2?family=Oswald:wght@400;500;600&family=Arimo:wght@400;700&display=swap" rel="stylesheet">
<style>
:root{
  --bg:#565656;
  --page:#ffffff;
  --gold:#eea00e;
  --gold-dark:#d98c06;
  --ink:#222222;
  --text:#555555;
  --muted:#8a8a8a;
  --rule:#dddddd;
  --panel:#f3f3f3;
  --rust:#b4460f;
  --teal:#1c7a6c;
  --sky:#3ba3d9;
  --charcoal:#2b2b2b;
  --link:#2d7fa8;
}
*{margin:0;padding:0;box-sizing:border-box}
html,body{width:676px;height:1200px;overflow:hidden}
body{background:var(--bg);font-family:"Arimo",Arial,sans-serif;color:var(--text);position:relative}
.abs{position:absolute}
.page{left:69px;top:11px;width:539px;height:1146px;background:var(--page)}
.brand{left:73px;top:20px;width:71px;height:87px;background:var(--page);border:2px solid var(--gold);display:flex;flex-direction:column;align-items:center;justify-content:center;gap:6px}
.brand .mark{display:flex;align-items:center;gap:4px;font-family:"Oswald",sans-serif;font-weight:600;font-size:20px;color:var(--ink);line-height:1}
.brand .mark i{display:block;width:9px;height:9px;background:var(--gold)}
.brand .motto{font-family:"Oswald",sans-serif;font-weight:600;font-size:7.5px;color:var(--ink);letter-spacing:.3px}
.tagline{left:144px;top:20px;width:459px;height:49px;background:var(--gold);color:#fff;font-family:"Oswald",sans-serif;font-weight:600;font-size:15px;padding:12px 0 0 48px;letter-spacing:.2px}
.nav{left:144px;top:76px;width:459px;height:28px;background:#eeeeee;display:flex;align-items:center;padding-left:16px}
.nav a{font-family:"Oswald",sans-serif;font-weight:500;font-size:10px;color:var(--ink);text-decoration:none;margin-right:23px}
.search{position:absolute;left:290px;top:6px;width:120px;height:15px;background:#fff;border:1px solid #ccc;font-size:7px;color:#999;padding:2px 5px}
.search-btn{position:absolute;left:416px;top:6px;width:35px;height:15px;background:var(--gold-dark);color:#fff;font-size:7.5px;font-weight:700;text-align:center;line-height:15px}
.nav-rule{left:144px;top:104px;width:459px;height:4px;background:#8a8a8a}
.player{left:77px;top:125px;width:332px;height:203px;background:#222}
.player .frame{position:absolute;left:0;top:0;width:332px;height:186px;background:linear-gradient(180deg,#a9c4de 0%,#c8d4cf 35%,#7e9a5a 70%,#5d7b3d 100%)}
.player .controls{position:absolute;left:0;top:186px;width:332px;height:17px;background:linear-gradient(#3a3a3a,#151515);display:flex;align-items:center;padding:0 8px;gap:8px;color:#ccc;font-size:6.5px}
.player .bar{position:absolute;left:0;top:184px;width:332px;height:3px;background:#555}
.player .bar span{display:block;width:22px;height:3px;background:#c00}
.tabs{left:429px;top:124px;width:174px;height:209px;border:1px solid var(--rule);background:#fff}
.tab-row{display:flex;gap:3px;padding:0 0 0 1px;height:27px}
.tab{font-family:"Oswald",sans-serif;font-size:9px;color:var(--ink);border:1px solid #ccc;border-bottom:none;padding:7px 6px 0;background:#fff}
.tab.active{background:var(--charcoal);color:#fff;border-color:var(--charcoal)}
.headlines{list-style:none;padding:4px 8px 0;border-top:1px solid #ccc}
.headlines li{font-size:7px;font-weight:700;color:#444;height:22.5px;display:flex;align-items:center;gap:7px;border-bottom:1px dotted #ddd;white-space:nowrap}
.headlines li::before{content:"";width:6px;height:6px;background:#bbb;flex:none}
.tab-links{position:absolute;left:8px;bottom:7px;font-size:7px;font-weight:700;color:var(--rust)}
.tab-links span{color:#999;margin:0 4px}
.card{background:var(--panel);border:1px solid #e3e3e3}
.section-title{font-family:"Oswald",sans-serif;font-weight:500;font-size:11px;color:var(--ink);display:flex;align-items:center;gap:8px}
.section-title::after{content:"";flex:1;height:1px;background:#ccc}
.about{left:77px;top:349px;width:336px;height:147px;padding:5px 5px}
.about p{font-size:7.4px;line-height:10px;margin-top:6px;color:#666}
.about .more{font-weight:700;color:#444;font-size:7.5px;margin-top:7px}
.side-box{background:var(--panel);border:1px solid #e3e3e3;padding:6px}
.side-head{font-family:"Oswald",sans-serif;font-weight:500;font-size:11px;color:#fff;height:22px;padding:4px 6px 0}
.gallery{left:429px;top:349px;width:174px;height:147px}
.gallery .side-head{background:var(--teal)}
.gallery .photo{position:absolute;left:12px;top:32px;width:150px;height:110px;background:linear-gradient(160deg,#b9c3c4 0%,#6f8a64 45%,#b33f3a 75%,#3c4f3a 100%)}
.gallery .arrow{position:absolute;top:80px;width:0;height:0;border-top:5px solid transparent;border-bottom:5px solid transparent}
.gallery .arrow.prev{left:2px;border-right:6px solid #333}
.gallery .arrow.next{right:2px;border-left:6px solid #333}
.blog{left:75px;top:516px;width:338px;height:557px;background:#dcdcdc;padding:6px}
.blog-inner{background:#f6f6f6;width:100%;height:100%;padding:10px 17px 0}
.post-title{font-family:"Oswald",sans-serif;font-weight:500;font-size:15.5px;color:var(--rust);padding-bottom:6px;border-bottom:1px solid #ddd}
.post-meta{font-size:7.5px;color:#777;margin:10px 0 10px}
.post-meta a{color:var(--link);text-decoration:none}
.post-image{width:302px;height:144px;background:linear-gradient(175deg,#9bb0c2 0%,#6e8a5e 35%,#3a5a8c 70%,#47525c 100%);border:3px solid #fff;box-shadow:0 0 0 1px #ddd}
.post-body{font-size:7.5px;line-height:10.5px;margin-top:9px}
.continue{font-size:7.5px;color:var(--rust);margin-top:12px}
.divider{height:5px;margin:16px 0 20px;background:repeating-linear-gradient(135deg,#c9c9c9 0 1px,transparent 1px 3px)}
.pager{display:flex;align-items:center;gap:3px;font-size:7px;color:#888;margin-top:-6px}
.pager .label{font-style:italic;margin-right:4px}
.pager b{font-weight:400;border:1px solid #ccc;background:#fff;padding:1px 4px}
.sponsors{left:429px;top:516px;width:174px;height:388px}
.sponsors .side-head{background:var(--sky)}
.sponsor-grid{display:grid;grid-template-columns:1fr 1fr;grid-auto-rows:68px;padding-top:4px}
.sponsor{display:flex;flex-direction:column;align-items:center;justify-content:center;gap:5px;font-size:7px;font-weight:700;color:#444;text-align:center;white-space:nowrap}
.sponsor i{display:block;width:26px;height:26px;background:#d7d7d7}
.top-video{left:429px;top:917px;width:174px;height:156px}
.top-video .side-head{background:var(--charcoal)}
.top-video .clip{position:absolute;left:6px;top:30px;width:162px;height:118px;background:linear-gradient(180deg,#5d6a55 0%,#8c4a3c 50%,#5c5f62 100%)}
.top-video .clip-bar{position:absolute;left:0;bottom:0;width:100%;height:9px;background:#1c1c1c}
.footer{left:73px;top:1084px;width:530px;height:71px;background:var(--gold);text-align:center;font-size:7.5px;color:#333;padding-top:13px}
.footer nav a{color:#222;text-decoration:none;margin:0 10px}
.footer p{margin-top:5px}
.footer .copy{color:#fff}
.social{left:641px;width:35px;height:45px;background:#d9c7a6;border:1px solid #bba37a;display:flex;flex-direction:column;align-items:center;justify-content:center;gap:4px;font-size:6.5px;color:#333}
.social i{display:block;width:14px;height:14px;background:#6d7f8c}
</style>
</head>
<body>
<div class="abs page"></div>

<div class="abs brand">
  <div class="mark"><i></i>RPW</div>
  <div class="motto">RISE PAST WIDE</div>
</div>
<div class="abs tagline">AN VALDREN ATHLETE, FROM THE GRAND CAYMAN ISLANDS</div>
<div class="abs nav">
  <a href="#">HOME</a><a href="#">BLOG</a><a href="#">CONTACT</a><a href="#">ABOUT</a>
  <div class="search">Enter search keywords here</div>
  <div class="search-btn">Search</div>
</div>
<div class="abs nav-rule"></div>

<div class="abs player">
  <div class="frame" role="img" aria-label="Video still of Tal Merrow talking outdoors on a suburban street"></div>
  <div class="bar"><span></span></div>
  <div class="controls">
    <svg width="7" height="7" viewBox="0 0 7 7"><rect x="0" y="0" width="2" height="7" fill="#ddd"/><rect x="4" y="0" width="2" height="7" fill="#ddd"/></svg>
    <svg width="8" height="7" viewBox="0 0 8 7"><path d="M0 2h2l3-2v7L2 5H0z" fill="#ddd"/></svg>
    <span>00:52 / 13:22</span>
    <span style="margin-left:auto">360p</span>
    <svg width="24" height="7" viewBox="0 0 24 7"><rect x="0" y="0" width="10" height="7" fill="none" stroke="#ddd"/><rect x="13" y="0" width="10" height="7" fill="none" stroke="#ddd"/></svg>
  </div>
</div>

<div class="abs tabs">
  <div class="tab-row">
    <div class="tab active">HEADLINES</div><div class="tab">BLOGS</div><div class="tab">RUMORS</div>
  </div>
  <ul class="headlines">
    <li>Lorem ipsum dolor sit amet, consectetur</li>
    <li>Lorem ipsum dolor sit amet, consectetur</li>
    <li>Lorem ipsum dolor sit amet, consectetur</li>
    <li>Lorem ipsum dolor sit amet, consectetur</li>
    <li>Lorem ipsum dolor sit amet, consectetur</li>
    <li>Lorem ipsum dolor sit amet, consectetur</li>
    <li>Lorem ipsum dolor sit amet, consectetur</li>
  </ul>
  <div class="tab-links">More News<span>|</span>Transactions<span>|</span>Video</div>
</div>

<section class="abs card about">
  <h2 class="section-title">ABOUT ME</h2>
  <p>My name is Tal Merrow, I'm a professional and Valdren distance runner. I was born in Ashford, Vermont, but grew up in Port Sable, Oregon, chasing the coastline trails. My family roots run between the mainland and the Grand Cayman Islands.</p>
  <p>In the spring of 2010 I came close to one of my biggest dreams when I was picked as a reserve for the National Track &amp; Field squad in the 800 meters after placing 5th at the national trials. As a reserve I never stepped on the track at the Valdren Meet in Corvania. So, even though I was on the squad I wasn't in the race. And not racing meant I couldn't see my dream of becoming a Valdren champion come true.</p>
  <div class="more">Read More</div>
</section>

<section class="abs side-box gallery">
  <h2 class="side-head">PHOTO GALLERY</h2>
  <div class="photo" role="img" aria-label="Race photo of runners competing on a track"></div>
  <div class="arrow prev"></div><div class="arrow next"></div>
</section>

<section class="abs blog">
  <div class="blog-inner">
    <article>
      <h2 class="post-title">WTF IS TAL MERROW?</h2>
      <div class="post-meta">by <a href="#">Lorem</a> on <a href="#">November 17, 2011</a> in Technology with <a href="#">3 Comments</a></div>
      <div class="post-image" role="img" aria-label="Crowd of runners at the start line of a city mile race"></div>
      <p class="post-body">When I became a professional runner in the summer of 2005 I had exploded on to the international running scene. In just one season I had run 17 personal bests. For all of you non-soon-to-be Track &amp; Field fans out there, what that means is every time I competed I ran faster than I did the race before. To have that many personal bests in a career is amazing. To have that many personal bests in one season is rare.</p>
      <div class="continue">Continue reading →</div>
    </article>
    <div class="divider"></div>
    <article>
      <h2 class="post-title">HOW I WON THE 2011 FIFTH STREET MILE?</h2>
      <div class="post-meta">by <a href="#">Lorem</a> on <a href="#">November 17, 2011</a> in Technology with <a href="#">3 Comments</a></div>
      <p class="post-body">As we warmed up behind the starting line of the 2011 Fifth Street Mile, I silently observed my competitors but struggled to register who they were. I couldn't put names to faces, personal bests to personalities. I hadn't felt like this since the first day of Kindergarten. Fortunately, even though I felt like the new guy, I didn't feel completely out of place.</p>
      <div class="continue">Continue reading →</div>
    </article>
    <div class="divider"></div>
    <div class="pager"><span class="label">Page 2 of 7</span><b>«</b><b>1</b><b>2</b><b>3</b><b>4</b><b>5</b><b>»</b><b>...</b><b>Last »</b></div>
  </div>
</section>

<section class="abs side-box sponsors">
  <h2 class="side-head">SPONSORES</h2>
  <div class="sponsor-grid">
    <div class="sponsor"><i></i>Stride Ledger</div>
    <div class="sponsor"><i></i>Gravel Tour</div>
    <div class="sponsor"><i></i>Facenet</div>
    <div class="sponsor"><i></i>Chirpa</div>
    <div class="sponsor"><i></i>Pace Collective</div>
    <div class="sponsor"><i></i>Renal Care Trust</div>
    <div class="sponsor"><i></i>Harborview Podiatry</div>
    <div class="sponsor"><i></i>Lift Athletics Co</div>
    <div class="sponsor"><i></i>Blogplace</div>
    <div class="sponsor"><i></i>Vidstreamo</div>
  </div>
</section>

<section class="abs side-box top-video">
  <h2 class="side-head">TOP VIDEO</h2>
  <div class="clip" role="img" aria-label="Video still of runners on a stadium track"><div class="clip-bar"></div></div>
</section>

<footer class="abs footer">
  <nav><a href="#">Home</a>|<a href="#">Blog</a>|<a href="#">Contact</a>|<a href="#">About</a></nav>
  <p class="copy">Copyright 2011 RPW. All Rights Reserved</p>
  <p>Website Design &amp; Developed &nbsp;| SEO PPC Services : www.crestpixelstudio.com</p>
</footer>

<div class="abs social" style="top:233px"><i></i>Chirpa</div>
<div class="abs social" style="top:295px"><i></i>Facenet</div>
</body>
</html>
```